Pelton|Marsh & Quillan business card contest

We need a logo for an upscale boutique diversified company involved in real estate, investments, cattle, and more. Our businesses DO NOT need to be reflected in the business card nor do we want them noted. This is our logo and colors and we love our logo and colors. Our logo looks best against a black background and we like to include the firm name in our logo usage. importantly, the names Pelton and Marsh are separated by | not / and we use an ampersand not the word and.
On the front of the card, we want to include:
company logo and name (Pelton|Marsh & Quillan)
on the back, we would definitely include:
address, email, cell #
logo and name (smaller size than front)

The variable will be location of individual name and title (mine for example is ) - whether on the front OR on the back. interested in variations from which to choose
Dr. Neil R. Whitcombe, CFA
Scientifique des Fusées Financières

we would like to use contemporary symbols for address, email address, cell # with an option for web site that we do not intend to use initially. we like two sided cards and believe this design should use four rounded corners with the standard size. we prefer thicker card stock and may look at metal.

```html
<!DOCTYPE html>
<html lang="en">
<head>
<meta charset="utf-8">
<title>Pelton|Marsh &amp; Quillan — Business Card</title>
<link href="https://fonts.googleapis.com/css2?family=Montserrat:wght@400;500&family=Kaushan+Script&display=swap" rel="stylesheet">
<style>
  :root {
    --backdrop: #b5b5b5;
    --card: #0c0c0c;
    --brand-gray: #6b6b6b;
    --accent: #e8862a;
    --ink-light: #efefef;
  }
  * { box-sizing: border-box; margin: 0; padding: 0; }
  html, body {
    width: 1154px; height: 1200px; overflow: hidden;
    background: var(--backdrop);
  }
  .canvas { position: relative; width: 1154px; height: 1200px; }
  .card {
    position: absolute; left: 163px; width: 806px; height: 459px;
    background: var(--card);
  }
  .card--front { top: 94px; }
  .card--back { top: 590px; }

  .brand {
    position: absolute; display: flex; flex-direction: column; align-items: center;
    font-family: "Montserrat", sans-serif; font-weight: 500; color: var(--brand-gray);
    white-space: nowrap;
  }
  .brand__square { background: var(--brand-gray); }
  .card--front .brand { left: 0; right: 0; top: 104px; gap: 34px; }
  .card--front .brand__square { width: 120px; height: 120px; }
  .card--front .brand__name { font-size: 36px; }
  .card--back .brand { left: 56px; width: 335px; top: 140px; gap: 22px; }
  .card--back .brand__square { width: 80px; height: 80px; }
  .card--back .brand__name { font-size: 21px; }

  .divider {
    position: absolute; left: 402px; top: 134px; width: 1.5px; height: 192px;
    background: var(--accent);
  }
  .contact { position: absolute; left: 425px; top: 130px; font-family: "Montserrat", sans-serif; color: var(--ink-light); }
  .contact__name {
    font-family: "Kaushan Script", cursive; font-size: 27px; color: var(--accent);
    line-height: 1; white-space: nowrap;
  }
  .contact__title { font-size: 16px; margin-top: 6px; }
  .contact__address { font-size: 18.5px; line-height: 26px; margin-top: 22px; margin-left: 2px; }
  .contact__lines { margin-top: 14px; }
  .contact__line { display: flex; align-items: center; gap: 9px; font-size: 18.5px; line-height: 26px; }
  .contact__icon { width: 19px; height: 19px; flex: none; }
</style>
</head>
<body>
<main class="canvas">
  <section class="card card--front" aria-label="Card front">
    <div class="brand">
      <span class="brand__square"></span>
      <span class="brand__name">Pelton|Marsh &amp; Quillan</span>
    </div>
  </section>

  <section class="card card--back" aria-label="Card back">
    <div class="brand">
      <span class="brand__square"></span>
      <span class="brand__name">Pelton|Marsh &amp; Quillan</span>
    </div>
    <span class="divider"></span>
    <div class="contact">
      <p class="contact__name">Dr. Neil R. Whitcombe, CFA</p>
      <p class="contact__title">Scientifique des Fusées Financières</p>
      <p class="contact__address">482 Harlow Ave. #17<br>Fairmont, AR 72140</p>
      <div class="contact__lines">
        <p class="contact__line">
          <svg class="contact__icon" viewBox="0 0 20 20" aria-hidden="true">
            <rect x="5" y="1" width="10" height="18" rx="2" fill="none" stroke="var(--accent)" stroke-width="2"/>
            <line x1="8" y1="15.5" x2="12" y2="15.5" stroke="var(--accent)" stroke-width="1.6"/>
          </svg>
          555.014.2273
        </p>
        <p class="contact__line">
          <svg class="contact__icon" viewBox="0 0 20 20" aria-hidden="true">
            <rect x="1" y="4" width="18" height="13" fill="var(--accent)"/>
            <polyline points="1,4 10,11 19,4" fill="none" stroke="var(--card)" stroke-width="1.6"/>
          </svg>
          info@peltonmarsh&amp;quillan.com
        </p>
      </div>
    </div>
  </section>
</main>
</body>
</html>
```